Coastal Sentinels Stationery Design Project

I am looking for a suitable stationary design for my company Coastal Sentinels Pty Ltd (ACN 508 214 396).

The requirements can be better explained by visiting my website
"coastal-sentinels.org"

I will be sending letters to Ministers of State and the Heads of Government Agencies so the theme needs to be formal and serious.

A theme with a shield or similar picking on the "guardian" concept would be appropriate

Target Market(s)

Ministers of State and Department Agency Heads and legal firms, the heads of Trustee Companies as well as Members of Coastal Sentinels

Industry/Entity Type

Government

Requirements
Must have
• Letterhead design is a priority - Business Card secondary

Must include tag line "Shielding your savings when the rest walk away" with a registered trade mark superscript at the end that is an R in a circle {Windows Alt +0174 on numeric keypad or Mac Option +R}.

Must include website address "Coastal-Sentinels.org" plus Email address "coastsentinel@fernmail.net

Company name "Coastal Sentinels Pty. Ltd." and Australian Company Number "ACN 508 214 396" needs to be shown more discretely

Address is "47 Brookfern Lane, Marlow Vale, 3281"
Nice to have
• A watermark is something to be considered

```html
<!DOCTYPE html>
<html lang="en">
<head>
<meta charset="utf-8">
<title>Coastal Sentinels Business Card</title>
<link rel="stylesheet" href="https://fonts.googleapis.com/css2?family=Source+Sans+3:ital,wght@0,400;0,600;1,400&display=swap">
<style>
  :root {
    --stage-left: #0f1010;
    --stage-right: #000000;
    --brand-blue: #1414ff;
    --brand-blue-deep: #0b0bd9;
    --brand-blue-panel: #1818e6;
    --card-white: #ffffff;
    --ink: #333333;
    --ink-dark: #111111;
    --label-blue: #2a2aff;
  }
  * { margin: 0; padding: 0; box-sizing: border-box; }
  html, body { width: 1200px; height: 849px; overflow: hidden; background: var(--stage-right); }
  .canvas {
    position: relative; width: 1200px; height: 849px; overflow: hidden;
    font-family: "Source Sans 3", "PT Sans", sans-serif;
    background: linear-gradient(to right, var(--stage-left) 0 539px, var(--stage-right) 539px 100%);
  }
  .card { position: absolute; left: 57px; width: 436px; overflow: hidden; }
  p { white-space: nowrap; }

  /* Front */
  .card-front { top: 87px; height: 258px; background: var(--card-white); }
  .card-front .top-band {
    position: absolute; left: 0; top: 0; width: 100%; height: 18px;
    background: linear-gradient(to right, var(--brand-blue) 0 273px, var(--brand-blue-deep) 273px 100%);
  }
  .holder { position: absolute; left: 9px; top: 56px; color: var(--label-blue); font-style: italic; }
  .holder .name { font-size: 11px; line-height: 14px; }
  .holder .designation { font-size: 9px; line-height: 12px; }
  .personal { position: absolute; left: 9px; top: 100px; color: var(--ink-dark); font-style: italic; font-size: 9px; line-height: 13px; }

  .lockup-small { position: absolute; left: 9px; top: 200px; display: flex; align-items: center; gap: 7px; }
  .lockup-small .mark { width: 24px; height: 28px; background: var(--brand-blue); flex: none; }
  .lockup-small .brand-name { font-size: 17px; font-weight: 600; color: var(--brand-blue-deep); line-height: 18px; }
  .lockup-small .tagline { font-size: 8px; color: var(--brand-blue-deep); line-height: 10px; }

  .contact { position: absolute; left: 232px; top: 172px; font-size: 10.5px; line-height: 12.6px; }
  .contact .row { display: flex; white-space: nowrap; }
  .contact .label { width: 41px; flex: none; text-align: right; padding-right: 3px; color: var(--label-blue); white-space: nowrap; }
  .contact .value { color: var(--ink); white-space: nowrap; }

  /* Back */
  .card-back {
    top: 386px; height: 258px;
    background: linear-gradient(to right, var(--brand-blue) 0 273px, var(--brand-blue-panel) 273px 100%);
  }
  .lockup-large { position: absolute; left: 14px; top: 94px; display: flex; align-items: center; }
  .lockup-large .mark { width: 48px; height: 56px; background: var(--card-white); flex: none; }
  .lockup-large .divider { width: 2px; height: 50px; background: var(--card-white); margin: 0 9px 0 17px; flex: none; }
  .lockup-large .brand-name { font-size: 29px; font-weight: 600; color: var(--card-white); line-height: 30px; letter-spacing: -0.3px; }
  .lockup-large .tagline { font-size: 15px; color: var(--card-white); line-height: 18px; }
  sup { font-size: 0.6em; line-height: 0; }
</style>
</head>
<body>
<main class="canvas">
  <section class="card card-front" aria-label="Business card front">
    <div class="top-band"></div>
    <div class="holder">
      <p class="name">Name</p>
      <p class="designation">Designation</p>
    </div>
    <div class="personal">
      <p>Mob +61 400 555 019</p>
      <p>email name@fernmail.net</p>
    </div>
    <div class="lockup-small">
      <div class="mark"></div>
      <div>
        <p class="brand-name">Coastal Sentinels</p>
        <p class="tagline">Shielding your savings when the rest walk away<sup>®</sup></p>
      </div>
    </div>
    <div class="contact">
      <div class="row"><span class="label"></span><span class="value">Coastal Sentinels Pty Ltd.</span></div>
      <div class="row"><span class="label"></span><span class="value">ACN 508 214 396</span></div>
      <div class="row"><span class="label">e-mail</span><span class="value">coastsentinel@fernmail.net</span></div>
      <div class="row"><span class="label">web</span><span class="value">www.coastal-sentinels.org</span></div>
      <div class="row"><span class="label">add</span><span class="value">47 Brookfern Lane,</span></div>
      <div class="row"><span class="label"></span><span class="value">Marlow Vale, 3281</span></div>
    </div>
  </section>

  <section class="card card-back" aria-label="Business card back">
    <div class="lockup-large">
      <div class="mark"></div>
      <div class="divider"></div>
      <div>
        <p class="brand-name">Coastal Sentinels</p>
        <p class="tagline">Shielding your savings when the rest walk away<sup>®</sup></p>
      </div>
    </div>
  </section>
</main>
</body>
</html>
```